Pool Screen Enclosure Building a Career Boot Camp!

Looking to Host a Boot Camp for people looking for a career or looking to change careers. We Design, Manufacture and Install Custom Pool Screen Enclosures. We have a training program to allow Non Experienced motivated people the chance at a great career that will provide a great living for them and their family. This will be a paid boot camp, week long, we provide all the initial training for them to make a transition into our business. This will be 5 days of training with a guaranteed job to start the following Monday.... This is good for both someone with no construction experience or someone with construction experience that wants to upgrade their current job.
Paid Boot Camp
transition to a full time job with great pay
Benefits include Health Insurance, Dental and Vision, 401K, we provide the tools and training.

```html
<!DOCTYPE html>
<html lang="en">
<head>
<meta charset="utf-8">
<title>Pool Screen Enclosure Career Boot Camp</title>
<link rel="stylesheet" href="https://fonts.googleapis.com/css2?family=Barlow+Condensed:wght@500;600;700&family=Barlow:wght@500;600&display=swap">
<style>
  :root{
    --backdrop:#2468ae;
    --paper:#ffffff;
    --ink:#1b1b1b;
    --green:#3fa535;
    --green-bright:#5cb83f;
    --yellow:#f5bb00;
    --white:#ffffff;
  }
  *{margin:0;padding:0;box-sizing:border-box}
  html,body{width:1200px;height:1200px;overflow:hidden;background:var(--backdrop)}
  .flyer{position:absolute;left:200px;top:82px;width:801px;height:1037px;background:var(--paper);overflow:hidden;font-family:"Barlow",sans-serif;color:var(--ink)}
  .shapes{position:absolute;left:0;top:0;width:801px;height:1037px}
  .brand{position:absolute;left:34px;top:66px;display:flex;align-items:center;gap:12px}
  .brand-dot{width:34px;height:34px;border-radius:50%;background:var(--green)}
  .brand-name{font-family:"Barlow Condensed",sans-serif;font-weight:700;font-size:34px;color:var(--green);line-height:1}
  .headline{position:absolute;left:37px;top:0;width:300px;font-family:"Barlow Condensed",sans-serif;font-weight:600;line-height:1;color:var(--green)}
  .headline span{position:absolute;left:0;white-space:nowrap}
  .headline .small{top:195px;font-size:38px}
  .headline .big{font-size:58px}
  .headline .line-two{top:238px}
  .headline .line-three{top:295px}
  .headline .accent{top:355px;font-size:39px;color:var(--yellow)}
  .services{position:absolute;left:39px;top:474px;height:147px;border-left:2px solid var(--ink);padding-left:27px;font-family:"Barlow Condensed",sans-serif;font-weight:600;font-size:31px;line-height:42.3px;color:var(--ink)}
  .services p{margin-top:-15px;white-space:nowrap}
  .services .hl{color:var(--green)}
  .points{position:absolute;left:36px;top:648px;width:660px;list-style:none}
  .points li{position:relative;padding-left:39px;font-size:15px;font-weight:500;line-height:22px;margin-bottom:12px}
  .points svg{position:absolute;left:0;top:10px;width:24px;height:24px}
  .details{position:absolute;left:40px;top:797px;width:580px;color:var(--white);font-size:14.6px;font-weight:500;line-height:21.8px}
  .details .hl{color:var(--green-bright)}
  .benefits{position:absolute;left:40px;top:891px;width:640px;color:var(--white);font-size:22px;font-weight:500;line-height:33px}
  .benefits .hl{color:var(--green-bright)}
  .web{position:absolute;left:410px;top:930px;width:200px;height:24px;border-radius:4px;background:var(--green-bright);border:1px solid #8fd46a;display:flex;align-items:center;justify-content:center;gap:6px;font-family:"Barlow Condensed",sans-serif;font-weight:700;font-size:15px;color:var(--ink)}
  .footer{position:absolute;left:32px;top:999px;display:flex;align-items:center;gap:10px;font-family:"Barlow Condensed",sans-serif;font-weight:700;font-size:18.5px;color:var(--white);white-space:nowrap}
  .footer .sep{width:1px;height:18px;background:var(--white);margin:0 6px}
</style>
</head>
<body>
<div class="flyer">
  <svg class="shapes" viewBox="0 0 801 1037">
    <defs>
      <linearGradient id="enclosureTone" x1="0" y1="0" x2="0" y2="1">
        <stop offset="0" stop-color="#c9ccd0"/>
        <stop offset="0.45" stop-color="#8d9398"/>
        <stop offset="0.7" stop-color="#5c6a55"/>
        <stop offset="1" stop-color="#6b7c86"/>
      </linearGradient>
      <linearGradient id="workerTone" x1="0" y1="0" x2="0" y2="1">
        <stop offset="0" stop-color="#b9c8c4"/>
        <stop offset="0.55" stop-color="#7f9a7a"/>
        <stop offset="1" stop-color="#4aa840"/>
      </linearGradient>
      <linearGradient id="roofTone" x1="0" y1="0" x2="0" y2="1">
        <stop offset="0" stop-color="#5d8fc6"/>
        <stop offset="0.5" stop-color="#a8b8c0"/>
        <stop offset="1" stop-color="#55a844"/>
      </linearGradient>
      <linearGradient id="planTone" x1="0" y1="0" x2="1" y2="1">
        <stop offset="0" stop-color="#b8b3a8"/>
        <stop offset="1" stop-color="#8c877c"/>
      </linearGradient>
    </defs>

    <rect class="dark-band" x="0" y="161" width="420" height="267" fill="#1b1b1b"/>

    <g role="img" aria-label="Photo of a finished screened pool enclosure at dusk overlooking a lake">
      <polygon points="492,0 801,0 801,499 787,511 374,353 345,241 384,101" fill="url(#enclosureTone)" stroke="#3fa535" stroke-width="4"/>
    </g>
    <g role="img" aria-label="Photo of an installer on a ladder fitting screen panels">
      <polygon points="455,303 584,378 584,526 455,600 327,526 327,378" fill="url(#workerTone)" stroke="#3fa535" stroke-width="4"/>
    </g>
    <g role="img" aria-label="Photo of two workers assembling an enclosure roof frame">
      <polygon points="651,384 756,445 756,567 651,627 544,567 544,445" fill="url(#roofTone)" stroke="#3fa535" stroke-width="4"/>
    </g>

    <path class="info-panel" d="M0,834 Q0,772 55,772 L801,772 L801,985 L0,985 Z" fill="#1b1b1b" stroke="#3fa535" stroke-width="6"/>
    <line x1="37" y1="880" x2="580" y2="880" stroke="#3fa535" stroke-width="2"/>
    <rect class="footer-band" x="0" y="985" width="801" height="52" fill="#3fa535"/>
    <polygon points="801,944 801,1037 725,985" fill="#5cb83f"/>

    <g role="img" aria-label="Photo of a team reviewing enclosure plans on site">
      <polygon points="700,716 785,764 785,862 700,910 615,862 615,764" fill="url(#planTone)" stroke="#3fa535" stroke-width="4"/>
    </g>
  </svg>

  <div class="brand">
    <span class="brand-dot"></span>
    <span class="brand-name">The Lanai Works</span>
  </div>

  <h1 class="headline">
    <span class="small">POOL SCREEN</span>
    <span class="big line-two">ENCLOSURE</span>
    <span class="big line-three">BUILDING A</span>
    <span class="accent">CAREER BOOT CAMP!</span>
  </h1>

  <div class="services">
    <p><span class="hl">We Design,</span><br><span class="hl">Manufacture</span> and<br>Install Custom<br>Pool Screen Enclosures.</p>
  </div>

  <ul class="points">
    <li><svg viewBox="0 0 24 24"><polygon points="12,1 20,5 23,12 20,19 12,23 4,19 1,12 4,5" fill="#3a3a3a"/><path d="M7 12.5l3.2 3.2L17 9" fill="none" stroke="#fff" stroke-width="2.4"/></svg>We have a training program to allow Non Experienced motivated people the chance at a<br>great career that will provide a great living for them and their family.</li>
    <li><svg viewBox="0 0 24 24"><polygon points="12,1 20,5 23,12 20,19 12,23 4,19 1,12 4,5" fill="#3a3a3a"/><path d="M7 12.5l3.2 3.2L17 9" fill="none" stroke="#fff" stroke-width="2.4"/></svg>This will be a paid boot camp, week long, we provide all the initial training for<br>them to make a transition into our business.</li>
  </ul>

  <p class="details">This will be <span class="hl">5 days of training</span> with a <span class="hl">guaranteed job</span> to start the following Monday....<br>This is good for both someone with no construction experience or someone<br>with construction experience that wants to upgrade their current job.</p>

  <p class="benefits"><span class="hl">Benefits include</span> Health Insurance, Dental and Vision, 401K,<br>we provide the tools and training.</p>

  <div class="web">
    <svg width="10" height="10" viewBox="0 0 10 10"><circle cx="5" cy="5" r="4.2" fill="none" stroke="#1b1b1b" stroke-width="1"/><path d="M1 5h8M5 1v8" stroke="#1b1b1b" stroke-width="1"/></svg>
    www.lanaiworks.com
  </div>

  <div class="footer">
    <svg width="14" height="18" viewBox="0 0 14 18"><path d="M7 0C3 0 0 3 0 7c0 5 7 11 7 11s7-6 7-11c0-4-3-7-7-7z" fill="#fff"/><circle cx="7" cy="7" r="2.6" fill="#3fa535"/></svg>
    <span>218 Harbor Palm Avenue, Fort Pierce FL 34950</span>
    <span class="sep"></span>
    <svg width="17" height="12" viewBox="0 0 17 12"><rect width="17" height="12" rx="1" fill="#fff"/><path d="M1 1l7.5 6L16 1" fill="none" stroke="#3fa535" stroke-width="1.5"/></svg>
    <span>772-555-0148 hello@lanaiworks.com</span>
  </div>
</div>
</body>
</html>
```